Advertising Portal Needs eBrochure

Hi Crowders! Our advertising portal, which focus on the new launches property, needs an online brochure to promote to potential advertisers the benefits of advertising their projects with us. These advertisers will be mainly real estate developers and agencies.

WHAT WE LOOKING FOR
We do not want over-fanciful designs that makes the content hard to read. The use of illustrations and graphics/symbols related to covered topics are encouraged. The overall design should portrait our advertising efficiency through online and social media means. Our website - www.brightkeyhomes.sg.

For draft purposes, just do up the front page, back page, and few inner pages, preferably to include one illustration chart (either on page 7/8). Size wise probably A5 portrait or landscape, for future printing into a booklet.

WORK COMPLETION AND PAYMENT
The $500 stated here is 50% of the payment. Upon getting a desired draft design, we will need you to work on the full content with slight amendments along the way. Once done, we will be paying the balance $500, and we will need the pdf file as well as the work file.

Let your design juice flow, and hope we can work with you!
Updates

Hi Crowders! Thank you for your submissions. We are closing the project as we've decided on a design. It's a pity we can only select one design, as there are a number of good works. Hope we will have a chance to work together on our upcoming projects. Cheers =)

Target Market(s)

Real estate developers, real estate agencies, and perhaps to an extent, individual property sales agent.

Industry/Entity Type

Advertising

Requirements
Should not have
• We prefer not to have much real people kind of stock images. Try not to use images from our portal as we do not have the ownerships. Instead, you can use stock images of property developments artist impression that gives a similar feel.

```html
<!DOCTYPE html>
<html lang="en">
<head>
<meta charset="utf-8">
<title>Bright Key Homes – Get More 4 Less</title>
<link rel="stylesheet" href="https://fonts.googleapis.com/css2?family=Montserrat:wght@400;700;800&family=Raleway:wght@300;600&display=swap">
<style>
  :root {
    --stage: #e4e4e4;
    --paper: #ffffff;
    --collage-light: #e8e8e8;
    --collage-dark: #8a8a8a;
    --brand-green: #5aa63c;
    --frame-green: #4f9a35;
    --ink-dark: #333333;
    --ink-grey: #5a5a5a;
    --accent-red: #c8181e;
    --skin-light: #e7c2a8;
    --skin-dark: #c9987a;
  }
  * { box-sizing: border-box; margin: 0; padding: 0; }
  html, body { width: 1200px; height: 800px; overflow: hidden; }
  body {
    background: var(--stage);
    font-family: "Montserrat", Arial, sans-serif;
    position: relative;
  }
  .cover {
    position: absolute;
    left: 340px; top: 32px;
    width: 520px; height: 736px;
    background: var(--paper);
    overflow: hidden;
    box-shadow: 0 6px 24px rgba(0,0,0,.18);
  }
  .cover__collage {
    position: absolute; inset: 0;
    background:
      linear-gradient(180deg, rgba(255,255,255,.55) 0%, rgba(255,255,255,.2) 40%, rgba(255,255,255,0) 100%),
      linear-gradient(135deg, var(--collage-light) 0%, #bdbdbd 45%, var(--collage-dark) 100%);
  }
  .brand {
    position: absolute; left: 0; right: 0; top: 70px;
    display: flex; flex-direction: column; align-items: center;
  }
  .brand__row { display: flex; align-items: center; gap: 10px; }
  .brand__mark {
    width: 22px; height: 22px;
    background: var(--ink-dark);
  }
  .brand__name {
    font-weight: 700; font-size: 30px;
    color: var(--ink-dark);
  }
  .brand__tagline {
    margin-top: 10px;
    font-weight: 400; font-size: 10px; letter-spacing: 1.4px;
    color: var(--ink-grey); text-transform: uppercase;
  }
  .frame {
    position: absolute; left: 62px; top: 212px;
    width: 392px; height: 392px;
    background: var(--frame-green);
  }
  .panel {
    position: absolute; left: 92px; top: 182px;
    width: 392px; height: 392px;
    background: var(--paper);
    overflow: hidden;
  }
  .hand {
    position: absolute;
    background: linear-gradient(135deg, var(--skin-light), var(--skin-dark));
  }
  .hand--top-left { left: 0; top: 0; width: 120px; height: 96px; border-radius: 0 0 48px 0; }
  .hand--bottom-right { right: 0; bottom: 0; width: 100px; height: 80px; border-radius: 48px 0 0 0; }
  .headline { position: absolute; inset: 0; font-weight: 800; }
  .headline__get {
    position: absolute; left: 0; right: 0; top: 56px;
    text-align: center;
    font-size: 46px; color: var(--ink-dark);
  }
  .headline__more {
    position: absolute; left: 34px; top: 98px;
    font-size: 80px; letter-spacing: -2px;
    color: var(--brand-green);
  }
  .headline__four {
    position: absolute; left: 60px; top: 170px;
    font-size: 80px; color: var(--brand-green);
  }
  .headline__less {
    position: absolute; left: 120px; top: 170px;
    font-size: 80px; letter-spacing: -2px;
    color: var(--ink-dark);
  }
  .subline {
    position: absolute; left: 24px; top: 270px;
    font-family: "Raleway", Arial, sans-serif;
    font-weight: 300; font-size: 15px; color: var(--ink-grey);
    line-height: 1.3; white-space: nowrap;
  }
  .subline strong { font-weight: 600; color: var(--accent-red); }
  .subline__second { display: block; padding-left: 110px; }
</style>
</head>
<body>
  <article class="cover">
    <div class="cover__collage" role="img" aria-label="Greyscale collage of condominium and property development photographs"></div>

    <header class="brand">
      <div class="brand__row">
        <span class="brand__mark"></span>
        <span class="brand__name">Bright Key Homes</span>
      </div>
      <p class="brand__tagline">New property launches, every day</p>
    </header>

    <div class="frame"></div>
    <section class="panel">
      <div class="hand hand--top-left" role="img" aria-label="Photograph of a hand forming the top-left corner of a frame"></div>
      <div class="hand hand--bottom-right" role="img" aria-label="Photograph of a hand forming the bottom-right corner of a frame"></div>

      <h1 class="headline">
        <span class="headline__get">Get</span>
        <span class="headline__more">MORE</span>
        <span class="headline__four">4</span>
        <span class="headline__less">LESS</span>
      </h1>

      <p class="subline">With Our <strong>Effective Marketing Packages</strong>
        <span class="subline__second">For Property Launches</span></p>
    </section>
  </article>
</body>
</html>
```